Business Consultancy Wordpress Design

Small business analysis consultancy.

Looking for a bold, clean design for Wordpress. Final site will only be a few pages, some contact information, services provided and a little background information. Potentially a blog.

Colours to be as per logo, with either black or white as the main colour.

Link is www.halvicadvisory.com

More details to be included in the best few days

Name - Halvic Consulting
Provides - Project Consultancy
Updates

Project Deadline Extended
Reason: I am going to be on holiday with little access to the web over 28/02 - 05/03 and am therefore extending the deadline

Target Market(s)

Business professionals

Industry/Entity Type

Business

Colors

Designer to choose colors to be used in the design.

Requirements
Must have
• Must contain the logo in the header
Footer must fit a 3 column layout in wordpress

Business style, royalty free stock images
Nice to have
• Would like the 1 or 2 column wordpress style layout
Should not have
• must not be blog or magazine style layout or look and feel

```html
<!DOCTYPE html>
<html lang="en">
<head>
<meta charset="utf-8">
<title>Halvic Consulting</title>
<link href="https://fonts.googleapis.com/css2?family=Open+Sans:wght@400;600;700&family=Roboto:wght@400;500&display=swap" rel="stylesheet">
<style>
:root{
  --blue:#0b8fd4;
  --green:#5aa52f;
  --ink:#3a4046;
  --text:#555b60;
  --muted:#7a7f84;
  --line:#dcdcdc;
  --card-grey:#efefef;
  --footer:#f4f4f4;
  --white:#ffffff;
}
*{margin:0;padding:0;box-sizing:border-box}
html,body{width:762px;height:1200px;overflow:hidden;background:var(--white)}
body{position:relative;font-family:"Open Sans",Arial,sans-serif;color:var(--text)}
.abs{position:absolute}

/* header */
.topline{left:0;top:0;width:762px;height:2px;background:linear-gradient(90deg,var(--green),var(--blue))}
.brand{display:flex;align-items:center;gap:7px;font-size:14px;font-weight:600;color:var(--ink);letter-spacing:.2px;text-transform:uppercase}
.brand-dot{width:22px;height:22px;border-radius:50%;background:var(--blue)}
.header-brand{left:101px;top:20px}
.nav{left:375px;top:24px;display:flex;align-items:center;font-size:8px;font-weight:600;color:#666}
.nav a{color:#666;text-decoration:none;margin-right:16px}
.nav .active{background:var(--blue);color:var(--white);padding:4px 6px;margin-right:6px}
.nav .spaced{margin-right:24px}
.lang{display:flex;align-items:center;gap:3px}
.flag{width:8px;height:5px;background:#c8102e;border:1px solid #1e3a8a}

/* hero */
.hero{left:0;top:60px;width:762px;height:271px;background:linear-gradient(90deg,#c9b8ac 0%,#a99182 30%,#6d5a50 55%,#c49a6c 75%,#e7e2dc 100%)}
.hero-caption{left:101px;top:155px;width:404px;height:82px;background:rgba(40,40,40,.55);padding:11px 14px}
.hero-caption h1{font-family:"Roboto",Arial,sans-serif;font-weight:500;font-size:20px;color:var(--white)}
.hero-caption p{font-family:"Roboto",Arial,sans-serif;font-size:12.5px;line-height:15px;color:#eee;margin-top:5px}

/* services */
.section-title{left:0;top:346px;width:762px;text-align:center;font-size:25px;color:var(--ink);font-weight:400}
.section-title b{font-weight:600}
.section-lead{left:125px;top:382px;width:512px;text-align:center;font-size:10px;line-height:14px;color:var(--muted)}
.card{width:146px;height:141px;border:1px solid var(--line);border-radius:2px;text-align:center;padding-top:16px;background:var(--white)}
.card.shaded{background:var(--card-grey);border-color:#d2d2d2}
.card svg{display:block;margin:0 auto;height:34px}
.card h3{font-size:14px;font-weight:600;color:var(--ink);margin-top:7px}
.card p{font-size:7.6px;line-height:11px;color:#666;padding:0 14px;margin-top:5px}
.divider{left:357px;top:765px;width:47px;height:1px;background:var(--line)}
.divider-dot{left:378px;top:763px;width:5px;height:5px;border-radius:50%;background:#ccc}

/* about + contact */
.h2{font-size:15px;color:var(--ink);font-weight:400}
.h2 span{color:var(--blue)}
.about{left:101px;top:790px;width:310px}
.about .intro{font-size:8px;line-height:12px;color:var(--blue);font-weight:600;margin-top:8px}
.about .body{font-size:7px;line-height:12px;color:#444;margin-top:9px}
.btn{display:inline-flex;align-items:center;justify-content:center;color:var(--white);font-weight:600;border-radius:2px;font-size:9.5px}
.btn-start{left:102px;top:941px;width:117px;height:31px;background:var(--green)}
.contact{left:444px;top:790px;width:216px}
.contact p{font-size:7px;line-height:12px;color:#444;margin-top:8px}
.field{border:1px solid #d8d8d8;background:#f7f7f7;border-radius:2px;font-size:7px;color:#666;padding:7px 8px}
.f-name{left:445px;top:848px;width:98px;height:24px}
.f-mail{left:551px;top:848px;width:109px;height:24px}
.f-msg{left:445px;top:880px;width:215px;height:67px}
.btn-submit{left:445px;top:955px;width:78px;height:24px;background:var(--blue)}

/* footer */
.footer{left:0;top:1005px;width:762px;height:157px;background:var(--footer);border-top:1px solid #e6e6e6;border-bottom:1px solid #e1e1e1}
.fcol h4{font-size:8.5px;color:var(--green);font-weight:600}
.fcol ul{list-style:none;margin-top:12px}
.fcol li{font-size:7px;color:#555;margin-bottom:7.5px}
.fcol li::before{content:"›";color:#888;margin-right:7px}
.fcol p{font-size:7px;line-height:10px;color:#555;margin-top:12px}
.news-input{margin-top:7px;width:124px;height:20px;border:1px solid #d8d8d8;background:var(--white);display:flex;align-items:center;justify-content:space-between;padding-left:9px;font-size:7px;color:#666}
.news-input i{width:17px;height:15px;background:var(--blue);margin-right:2px;display:flex;align-items:center;justify-content:center}
.phone-line{display:flex;align-items:center;gap:4px;font-size:9.5px;color:#555;margin-top:4px}
.socials{margin-top:6px;width:84px;height:22px;border:1px solid #d8d8d8;background:var(--white);display:flex;align-items:center;justify-content:center;gap:3px}
.socials span{width:12px;height:12px;border:1px solid #555;border-radius:50%}
.bottom-brand{left:101px;top:1171px}
.bottom-brand .brand-dot{width:18px;height:18px}
.bottom-brand{font-size:11.5px}
.copyright{left:471px;top:1175px;width:189px;text-align:right;font-size:7px;color:#777}
</style>
</head>
<body>
<div class="abs topline"></div>

<header>
  <div class="abs brand header-brand"><span class="brand-dot"></span>Halvic Consulting</div>
  <nav class="abs nav">
    <a class="active">News</a>
    <a class="spaced">Services</a>
    <a>Projects</a>
    <a>Career</a>
    <a>About</a>
    <a>Contact</a>
    <span class="lang">▾ <span class="flag"></span> English</span>
  </nav>
</header>

<section>
  <div class="abs hero" role="img" aria-label="Photo of a smiling businesswoman in a dark suit in a blurred office with colleagues"></div>
  <div class="abs hero-caption">
    <h1>We make Simple, Faster and Easier</h1>
    <p>Quisque sed ipsum nec felis dignissim aliquet. Donec ut mauris risus. Nam iaculis imperdiet erat semper bibendum.</p>
  </div>
</section>

<section>
  <h2 class="abs section-title"><b>What we can do</b> better for <b>You</b></h2>
  <p class="abs section-lead">Lorem ipsum dolor sit amet, consectetur adipiscing elit. Pellentesque sed odio sed mi suscipit commodo. Integer dictum neque blandit orci ullamcorper hendrerit.</p>

  <div class="abs card shaded" style="left:140px;top:436px">
    <svg viewBox="0 0 40 34"><circle cx="15" cy="13" r="9" fill="none" stroke="var(--blue)" stroke-width="3.5"/><line x1="22" y1="20" x2="33" y2="30" stroke="var(--blue)" stroke-width="4.5" stroke-linecap="round"/></svg>
    <h3>Planning</h3>
    <p>Lorem ipsum dolor sit amet, con-sectetur adipiscing elit. Praesent tristique magna quam, a volutpat justo pharetra ut.</p>
  </div>
  <div class="abs card" style="left:308px;top:436px">
    <svg viewBox="0 0 40 34"><rect x="9" y="3" width="20" height="28" fill="none" stroke="var(--ink)" stroke-width="2"/><line x1="13" y1="10" x2="24" y2="10" stroke="var(--ink)" stroke-width="1.5"/><line x1="13" y1="15" x2="22" y2="15" stroke="var(--ink)" stroke-width="1.5"/><line x1="13" y1="20" x2="20" y2="20" stroke="var(--ink)" stroke-width="1.5"/><line x1="22" y1="26" x2="34" y2="6" stroke="var(--ink)" stroke-width="3"/></svg>
    <h3>Management</h3>
    <p>Lorem ipsum dolor sit amet, con-sectetur adipiscing elit. Praesent tristique magna quam, a volutpat justo pharetra ut.</p>
  </div>
  <div class="abs card shaded" style="left:476px;top:436px">
    <svg viewBox="0 0 40 34"><rect x="5" y="3" width="30" height="21" rx="1" fill="var(--green)"/><rect x="8" y="6" width="24" height="15" fill="#7cc05a"/><rect x="18" y="24" width="4" height="5" fill="var(--green)"/><circle cx="20" cy="31" r="3" fill="var(--green)"/></svg>
    <h3>Training</h3>
    <p>Lorem ipsum dolor sit amet, con-sectetur adipiscing elit. Praesent tristique magna quam, a volutpat justo pharetra ut.</p>
  </div>

  <div class="abs card" style="left:140px;top:597px">
    <svg viewBox="0 0 50 34"><circle cx="12" cy="11" r="5" fill="var(--green)"/><path d="M3 30c0-9 4-13 9-13s9 4 9 13z" fill="var(--green)"/><circle cx="38" cy="11" r="5" fill="var(--green)"/><path d="M29 30c0-9 4-13 9-13s9 4 9 13z" fill="var(--green)"/><circle cx="25" cy="9" r="6" fill="var(--green)"/><path d="M15 31c0-10 4-15 10-15s10 5 10 15z" fill="var(--green)"/></svg>
    <h3>Responsibility</h3>
    <p>Lorem ipsum dolor sit amet, con-sectetur adipiscing elit. Praesent tristique magna quam, a volutpat justo pharetra ut.</p>
  </div>
  <div class="abs card shaded" style="left:308px;top:597px">
    <svg viewBox="0 0 40 34"><path d="M8 3l6 0 3 8-4 3c2 5 5 8 10 10l3-4 8 3 0 6c0 2-2 3-4 3C16 32 7 22 6 6c0-2 1-3 2-3z" fill="var(--ink)"/></svg>
    <h3>Support</h3>
    <p>Lorem ipsum dolor sit amet, con-sectetur adipiscing elit. Praesent tristique magna quam, a volutpat justo pharetra ut.</p>
  </div>
  <div class="abs card" style="left:476px;top:597px">
    <svg viewBox="0 0 54 34"><rect x="2" y="5" width="7" height="26" fill="var(--blue)"/><rect x="45" y="5" width="7" height="26" fill="var(--blue)"/><path d="M10 9h12l8-3 14 4v13l-10 7-10-2-14-6z" fill="var(--blue)"/><path d="M20 14l8 5M24 11l8 6" stroke="var(--white)" stroke-width="1.5"/></svg>
    <h3>Meetings</h3>
    <p>Lorem ipsum dolor sit amet, con-sectetur adipiscing elit. Praesent tristique magna quam, a volutpat justo pharetra ut.</p>
  </div>

  <div class="abs divider"></div>
  <div class="abs divider-dot"></div>
</section>

<section>
  <div class="abs about">
    <h2 class="h2">Learn more <span>about us and our Services...</span></h2>
    <p class="intro">Lorem ipsum dolor sit amet, consectetur adipiscing elit. Pellentesque sed odio sed mi suscipit commodo. Integer dictum neque blandit orci ullamcorper.</p>
    <p class="body">Lorem ipsum dolor sit amet, consectetur adipiscing elit. Pellentesque sed odio sed mi suscipit commodo. Integer dictum neque blandit orci ullamcorper hendrerit. Sed eget diam mollis, viverra neque gravida, eleifend elit. Vestibulum eu sagittis metus. Fusce sit amet neque pharetra, lobortis tellus non, lobortis sem. Fusce orci massa, scelerisque bibendum metus sed, luctus sagittis lorem. Curabitur sollicitudin justo sed mauris aliquet, condimentum pretium arcu mollis. Nunc blandit sem fringilla velit imperdiet, non blandit augue ultrices. Vestibulum mattis orci ut eros ultrices consectetur. Proin rutrum tellus et adipiscing sollicitudin.</p>
  </div>
  <div class="abs btn btn-start">Let’s Get Started &nbsp;›</div>

  <div class="abs contact">
    <h2 class="h2">Quick <span>Contact</span></h2>
    <p>Praesent nec mauris hendrerit, luctus ante vitae, suscipit lacus. Class aptent taciti sociosqu inceptos himenaeos.</p>
  </div>
  <div class="abs field f-name">Full Name</div>
  <div class="abs field f-mail">Email Address</div>
  <div class="abs field f-msg">Type your Message</div>
  <div class="abs btn btn-submit">Submit Now &nbsp;›</div>
</section>

<footer>
  <div class="abs footer"></div>
  <div class="abs fcol" style="left:101px;top:1041px">
    <h4>Quick Links</h4>
    <ul><li>News</li><li>Services</li><li>Projects</li><li>Career</li><li>Contact</li></ul>
  </div>
  <div class="abs fcol" style="left:185px;top:1041px">
    <h4>About Us</h4>
    <ul><li>Who we are</li><li>In the press</li><li>Partners</li><li>Terms and Conditions</li></ul>
  </div>
  <div class="abs fcol" style="left:298px;top:1041px">
    <h4>Support</h4>
    <ul><li>Support Portal</li><li>Knowledge</li><li>Tutorials</li><li>Facilities</li></ul>
  </div>
  <div class="abs fcol" style="left:392px;top:1041px;width:130px">
    <h4>Subscribe to our Newsletter</h4>
    <p>Subscribe to new products, services and stuff.</p>
    <div class="news-input">Enter Email Id<i><svg width="7" height="9" viewBox="0 0 7 9"><path d="M1 1l4 3.5L1 8" fill="none" stroke="#fff" stroke-width="1.5"/></svg></i></div>
  </div>
  <div class="abs fcol" style="left:543px;top:1041px;width:130px">
    <h4>Contact Info</h4>
    <p>27 Arden Row, Marlow Bridge, UK</p>
    <div class="phone-line"><svg width="9" height="9" viewBox="0 0 9 9"><rect width="9" height="9" rx="1" fill="#555"/><path d="M2.5 2h1.3l.6 1.6-.8.6c.4 1 1 1.6 2 2l.6-.8 1.6.6V7.3C5 7.3 2.5 5 2.5 2z" fill="#fff"/></svg>+1 555 210 4836</div>
    <div class="socials"><span></span><span></span><span></span><span></span><span></span></div>
  </div>

  <div class="abs brand bottom-brand"><span class="brand-dot"></span>Halvic Consulting</div>
  <div class="abs copyright">Copyright © 2014 Halvic Consultancy. All Rights Reserved</div>
</footer>
</body>
</html>
```